Private Optometric Practice Needs new Presentation Folders/Stationary

We recently moved our office and are looking to refresh our presentation folders and stationary. I tend to prefer simple, clean designs. We are a full scope optometric practice provide high quality eyewear, custom contact lenses, along with emergency care and treatment for dry eyes. We communicate with a lot of other doctors and want to exude professionalism. I have attached 2 versions of our logo.

Target Market(s)

Familys

Industry/Entity Type

Eyecare

Font styles to use
Sans Serif

Colors
0054AA
0677BA
7BADD7
CADEEF
E8F1F8

Requirements
Nice to have
• Bifold, areas to put information about practice, welcome letter

```html
<!DOCTYPE html>
<html lang="en">
<head>
<meta charset="utf-8">
<title>Lumen Eyecare — Stationery Set</title>
<link href="https://fonts.googleapis.com/css2?family=Montserrat:wght@300;400;600&display=swap" rel="stylesheet">
<style>
  :root {
    --backdrop: #d3d3d3;
    --paper: #f5f5f6;
    --paper-white: #ffffff;
    --slate: #52525a;
    --ink: #2b2b30;
    --ink-soft: #55555c;
    --brand-blue: #4aa8dc;
    --rule-light: #e6e6ea;
    --divider: #9a9aa0;
  }
  * { box-sizing: border-box; margin: 0; padding: 0; }
  html, body {
    width: 1200px; height: 1200px; overflow: hidden;
    background: var(--backdrop);
    font-family: "Montserrat", sans-serif;
  }
  .sheet-set { position: relative; width: 1200px; height: 1200px; }

  /* Letterheads */
  .letterhead {
    position: absolute; top: 90px; width: 400px; height: 566px;
    background: var(--paper); color: var(--ink);
  }
  .letterhead--slate { left: 180px; background: var(--slate); color: var(--rule-light); }
  .letterhead--white { left: 620px; }
  .letterhead__rule {
    position: absolute; top: 40px; width: 108px; height: 1px; background: currentColor;
  }
  .letterhead__rule--left { left: 0; }
  .letterhead__rule--right { right: 0; }
  .brand {
    position: absolute; left: 0; right: 0; text-align: center;
  }
  .brand__dot {
    display: block; margin: 0 auto; border-radius: 50%; background: var(--brand-blue);
  }
  .brand__name {
    display: block; font-weight: 300; white-space: nowrap; color: currentColor;
  }
  .letterhead .brand { top: 14px; }
  .letterhead .brand__dot { width: 18px; height: 18px; }
  .letterhead .brand__name { margin-top: 10px; font-size: 13px; letter-spacing: 4px; padding-left: 4px; }

  .contact {
    position: absolute; display: flex; gap: 13px;
    font-weight: 400; color: currentColor;
  }
  .contact__address { text-align: right; }
  .letterhead .contact {
    top: 522px; left: 0; right: 0; font-size: 6.6px; line-height: 11.5px; letter-spacing: 0.3px;
  }
  .letterhead .contact__address { width: 192px; padding-top: 6px; }
  .letterhead--white .contact { color: var(--ink-soft); }

  /* Envelope */
  .envelope {
    position: absolute; left: 80px; top: 696px; width: 640px; height: 323px;
    background: var(--paper-white); color: var(--ink);
  }
  .envelope .brand { left: 36px; right: auto; top: 250px; width: 90px; }
  .envelope .brand__dot { width: 12px; height: 12px; }
  .envelope .brand__name { margin-top: 6px; font-size: 7.5px; letter-spacing: 1.6px; }
  .envelope .contact {
    left: 160px; top: 252px; font-size: 5.6px; line-height: 9.5px; color: var(--ink-soft);
  }
  .envelope .contact__address { width: 131px; padding-top: 5px; }

  /* Business card */
  .business-card {
    position: absolute; left: 760px; top: 745px; width: 360px; height: 225px;
    background: var(--paper-white); color: var(--ink);
  }
  .business-card .brand { left: 0; right: auto; width: 154px; top: 80px; }
  .business-card .brand__dot { width: 22px; height: 22px; }
  .business-card .brand__name { margin-top: 10px; font-size: 11px; letter-spacing: 2.5px; }
  .business-card__divider {
    position: absolute; left: 158px; top: 36px; width: 1px; height: 152px; background: var(--divider);
  }
  .business-card__details { position: absolute; left: 178px; top: 64px; color: var(--ink-soft); }
  .business-card__name {
    font-size: 9px; font-weight: 600; color: var(--ink); letter-spacing: 0.3px; margin-bottom: 16px;
  }
  .business-card__line { font-size: 6.4px; line-height: 9.5px; text-transform: uppercase; }
  .business-card__lines { margin-bottom: 20px; }
  .business-card__row { display: flex; align-items: center; gap: 5px; }
  .business-card__row svg { width: 7px; height: 7px; flex: none; }
</style>
</head>
<body>
<main class="sheet-set">

  <section class="letterhead letterhead--slate" aria-label="Letterhead, dark version">
    <span class="letterhead__rule letterhead__rule--left"></span>
    <span class="letterhead__rule letterhead__rule--right"></span>
    <div class="brand"><span class="brand__dot"></span><span class="brand__name">LUMEN EYECARE</span></div>
    <div class="contact">
      <div class="contact__address">4120 Maple Grove Dr. Suite B<br>Fairhaven, MI 48210</div>
      <div class="contact__lines">Phone: (555) 310-4821<br>Fax: (555) 310-4830<br>www.mylumeneyecare.com</div>
    </div>
  </section>

  <section class="letterhead letterhead--white" aria-label="Letterhead, light version">
    <span class="letterhead__rule letterhead__rule--left"></span>
    <span class="letterhead__rule letterhead__rule--right"></span>
    <div class="brand"><span class="brand__dot"></span><span class="brand__name">LUMEN EYECARE</span></div>
    <div class="contact">
      <div class="contact__address">4120 Maple Grove Dr. Suite B<br>Fairhaven, MI 48210</div>
      <div class="contact__lines">Phone: (555) 310-4821<br>Fax: (555) 310-4830<br>www.mylumeneyecare.com</div>
    </div>
  </section>

  <section class="envelope" aria-label="Envelope">
    <div class="brand"><span class="brand__dot"></span><span class="brand__name">LUMEN EYECARE</span></div>
    <div class="contact">
      <div class="contact__address">4120 Maple Grove Dr. Suite B<br>Fairhaven, MI 48210</div>
      <div class="contact__lines">Phone: (555) 310-4821<br>Fax: (555) 310-4830<br>www.mylumeneyecare.com</div>
    </div>
  </section>

  <section class="business-card" aria-label="Business card">
    <div class="brand"><span class="brand__dot"></span><span class="brand__name">LUMEN EYECARE</span></div>
    <span class="business-card__divider"></span>
    <div class="business-card__details">
      <p class="business-card__name">DANIEL WHITMORE, O.D.</p>
      <div class="business-card__lines">
        <p class="business-card__line">4120 Maple Grove Dr.</p>
        <p class="business-card__line">Suite B</p>
        <p class="business-card__line">Fairhaven, MI 48210</p>
      </div>
      <p class="business-card__line business-card__row">
        <svg viewBox="0 0 10 10" aria-hidden="true"><path d="M2 1 L4 1 L4.6 3.2 L3.4 4 Q4.3 5.8 6 6.6 L6.8 5.4 L9 6 L9 8 Q8.5 9 7.5 9 Q1 8 1 2.5 Q1 1.5 2 1 Z" fill="currentColor"/></svg>
        555-310-4821
      </p>
      <p class="business-card__line business-card__row">
        <svg viewBox="0 0 10 10" aria-hidden="true"><circle cx="5" cy="5" r="4" fill="none" stroke="currentColor" stroke-width="1"/><path d="M1 5 H9 M5 1 Q2.6 5 5 9 M5 1 Q7.4 5 5 9" fill="none" stroke="currentColor" stroke-width="0.8"/></svg>
        www.mylumeneyecare.com
      </p>
    </div>
  </section>

</main>
</body>
</html>
```